Business Card needed for Drainor, a growing Septic Service company

Drainor, a growing local septic service company in Pennsylvania, needs updated business cards. We'd like the business card to feature our logo and communicate that we provide Septic Pumping, Installations/Repairs, Restroom Rentals, and 24/7 Emergency Service. The business card should be eye-catching, bold, and clean/simple. We have been in business almost 10 years and would like to expand and update our business brand and image.

Target Market(s)

Residential and Commercial, New and Current Homeowners

Industry/Entity Type

Service

Contact Information for Business Card

Contact on the business card should be: Dean Harlow Owner & Operator
Phone: 610-555-0187
Email: service@drainor-example.com
Website: www.drainor-example.com
Address: 812 Millbrook Lane Fernvale PA 18990

Font styles to use
Sans Serif

Colors

Designer to choose colors to be used in the design.

Requirements
Must have
• Feature logo on both side of business card.
Nice to have
• We envision the contact information on one side and our services listed on the other side. Utilize the green from the symbol in our logo as part of the design, overall design color scheme should be white, grey, black.

```html
<!DOCTYPE html>
<html lang="en">
<head>
<meta charset="utf-8">
<title>Drainor Business Card</title>
<link rel="stylesheet" href="https://fonts.googleapis.com/css2?family=Fira+Sans:wght@400;600;800&display=swap">
<style>
  :root {
    --backdrop: #9a9a9a;
    --charcoal: #2f3032;
    --charcoal-deep: #262729;
    --charcoal-mid: #38393b;
    --paper: #e2e2e2;
    --ink: #1b1b1b;
    --ink-soft: #3a3a3a;
    --lime: #7dbb3f;
    --white: #f4f4f4;
  }
  * { margin: 0; padding: 0; box-sizing: border-box; }
  html, body {
    width: 1200px; height: 900px; overflow: hidden;
    background: var(--backdrop);
    font-family: "Fira Sans", sans-serif;
  }
  .card {
    position: absolute; left: 363px;
    width: 474px; height: 270px;
    border-radius: 22px; overflow: hidden;
  }
  .card--services { top: 145px; background: var(--charcoal); }
  .card--contact  { top: 484px; background: var(--paper); }

  .pattern-field {
    position: absolute; inset: 0;
    background: linear-gradient(180deg, var(--charcoal-mid) 0%, var(--charcoal) 60%, var(--charcoal-deep) 100%);
  }

  .brand { position: absolute; display: flex; align-items: center; }
  .brand__square { background: var(--lime); flex: none; }
  .brand__name { font-weight: 800; text-transform: uppercase; letter-spacing: 1px; line-height: 1; }

  .card--services .brand { left: 110px; top: 113px; }
  .card--services .brand__square { width: 44px; height: 44px; margin-right: 10px; }
  .card--services .brand__name { font-size: 45px; color: var(--white); }

  .services {
    position: absolute; left: 0; right: 0; top: 229px;
    text-align: center; font-size: 11px; color: var(--white);
    letter-spacing: .2px; white-space: nowrap;
  }
  .services__sep {
    display: inline-block; width: 1.5px; height: 13px;
    background: var(--lime); margin: 0 4px; vertical-align: -2px;
  }

  .card--contact .brand { left: 245px; top: 53px; }
  .card--contact .brand__square { width: 30px; height: 33px; margin-right: 8px; }
  .card--contact .brand__name { font-size: 31px; color: var(--ink); }

  .person { position: absolute; left: 38px; top: 51px; }
  .person__name { font-size: 14px; font-weight: 600; color: var(--lime); text-transform: uppercase; letter-spacing: .3px; }
  .person__role { font-size: 11px; color: var(--ink-soft); margin-top: 2px; letter-spacing: .2px; }

  .address { position: absolute; left: 38px; top: 97px; font-size: 11px; line-height: 15px; color: var(--ink-soft); }

  .contacts { position: absolute; left: 38px; top: 141px; list-style: none; font-size: 11px; line-height: 15px; color: var(--ink-soft); }
  .contacts__item { display: flex; align-items: center; }
  .contacts__icon { width: 9px; height: 9px; margin-right: 6px; flex: none; }

  .wave { position: absolute; left: 0; bottom: 0; width: 474px; height: 270px; }
</style>
</head>
<body>

<section class="card card--services" aria-label="Card front">
  <div class="pattern-field" role="img" aria-label="Faint repeating brand-symbol pattern on dark background"></div>
  <div class="brand">
    <span class="brand__square"></span>
    <span class="brand__name">Drainor</span>
  </div>
  <p class="services">Septic Pumping<span class="services__sep"></span>Installations/Repairs<span class="services__sep"></span>Restroom Rentals<span class="services__sep"></span>24/7 Emergency Service</p>
</section>

<section class="card card--contact" aria-label="Card back">
  <div class="person">
    <h1 class="person__name">Dean Harlow</h1>
    <p class="person__role">Owner &amp; Operator</p>
  </div>
  <p class="address">812 Millbrook Lane<br>Fernvale PA 18990</p>
  <ul class="contacts">
    <li class="contacts__item">
      <svg class="contacts__icon" viewBox="0 0 10 10"><path d="M2 0.5 L3.6 2.6 L2.7 3.6 C3.3 5 4.6 6.4 6.2 7.2 L7.2 6.3 L9.4 7.8 L8.4 9.5 C4.5 9.3 0.7 5.4 0.5 1.5 Z" fill="#7dbb3f"/></svg>
      610-555-0187
    </li>
    <li class="contacts__item">
      <svg class="contacts__icon" viewBox="0 0 10 10"><rect x="0.5" y="2" width="9" height="6.5" fill="#7dbb3f"/><path d="M0.8 2.3 L5 5.6 L9.2 2.3" fill="none" stroke="#e2e2e2" stroke-width="0.9"/></svg>
      service@drainor-example.com
    </li>
    <li class="contacts__item">
      <svg class="contacts__icon" viewBox="0 0 10 10"><circle cx="5" cy="5" r="4.3" fill="#7dbb3f"/><g fill="none" stroke="#e2e2e2" stroke-width="0.6"><ellipse cx="5" cy="5" rx="1.8" ry="4.3"/><line x1="0.7" y1="5" x2="9.3" y2="5"/><line x1="1.5" y1="3" x2="8.5" y2="3"/><line x1="1.5" y1="7" x2="8.5" y2="7"/></g></svg>
      www.drainor-example.com
    </li>
  </ul>
  <svg class="wave" viewBox="0 0 474 270" aria-hidden="true">
    <path d="M0,212 C60,240 130,248 210,238 C290,228 340,204 400,205 C440,206 460,212 474,218 L474,270 L0,270 Z" fill="#2a2b2d"/>
    <path d="M0,222 C70,252 150,258 230,244 C300,230 350,203 410,201 C445,200 462,205 474,208 L474,270 L0,270 Z" fill="#7dbb3f"/>
    <path d="M0,232 C70,262 150,266 230,254 C300,242 350,215 410,213 C445,212 462,218 474,222 L474,270 L0,270 Z" fill="#343537"/>
    <path d="M120,270 C220,262 300,236 370,224 C420,216 455,224 474,236 L474,270 Z" fill="#2b2c2e"/>
  </svg>
  <div class="brand">
    <span class="brand__square"></span>
    <span class="brand__name">Drainor</span>
  </div>
</section>

</body>
</html>
```